School Learner profile graphic representation

I have a set of ideas around communicating our school 'learner profile'. These represent the attitudes, habits and dispositions we are trying to develop through our curriculum and wider enrichment programme. I want the links between the ideas and concepts to be represented in some form of an inforgraphic which can be published and displayed for the whole community to connect with. we run two schools and want the profile to represent for both.

Target Market(s)

Students, Parents, Teachers, Wider community in education

Industry/Entity Type

Education

Font styles to use
Other font styles liked:
• Johnson p22

Colors

Designer to choose colors to be used in the design.

Requirements
Must have
• See my diagram in the ppt.
• The statements Aspiration, Agency, Agility, Altitude with the supporting descriptions. Ideally the values in the center is also represented. The two school logos should also be present somehow (both emblems at least). Let me know if the full logo files are required
Nice to have
• the numbering shown in my diagram is not absolutely necessary is it is not necessarily a linear process and rather cyclical and cross reinforcing

```html
<!DOCTYPE html>
<html lang="en">
<head>
<meta charset="utf-8">
<title>Envisioning Our Learners</title>
<link href="https://fonts.googleapis.com/css2?family=Prompt:wght@300;400;500;600&family=Hind:wght@400;500&display=swap" rel="stylesheet">
<style>
  :root {
    --bg: #f1f2f4;
    --brand-red: #e0262b;
    --ink: #111111;
    --gold-top: #f8bf34;
    --gold-bottom: #e08a1c;
    --gold-line: #fbd97a;
    --violet-top: #8b50f0;
    --violet-bottom: #5e32c6;
    --violet-line: #b69af0;
    --rose-top: #f45c9b;
    --rose-bottom: #d63a7a;
    --rose-line: #f39cc0;
    --aqua-top: #4eeaf7;
    --aqua-bottom: #1fb9cf;
    --aqua-line: #8fe8f2;
    --teal-line: #1a9aaa;
    --core: #dedede;
  }
  * { box-sizing: border-box; margin: 0; padding: 0; }
  html, body { width: 1200px; height: 755px; overflow: hidden; background: var(--bg); }
  body { font-family: "Prompt", sans-serif; color: var(--ink); position: relative; }

  .school-mark { position: absolute; display: flex; align-items: center; gap: 10px; }
  .school-mark .dot { width: 62px; height: 62px; border-radius: 50%; background: var(--brand-red); flex: none; }
  .school-mark .name { color: var(--brand-red); font-weight: 500; font-size: 19px; line-height: 1.15; letter-spacing: .02em; }
  .school-mark--primary { left: 191px; top: 44px; }
  .school-mark--community { left: 786px; top: 44px; }

  .rule { position: absolute; left: 3px; right: 0; top: 135px; height: 3px; background: var(--brand-red); }

  .page-title { position: absolute; left: 194px; top: 156px; font-weight: 500; font-size: 42px; line-height: 1.08; }

  .scene-art { position: absolute; }
  .scene-art--summit { left: 756px; top: 224px; width: 262px; height: 112px; border-radius: 8px;
    background: linear-gradient(180deg, #e4e5e8 0%, #9a9ca0 100%); }
  .scene-art--compass { left: 324px; top: 584px; width: 98px; height: 98px; border-radius: 50%;
    background: radial-gradient(circle, #6fb0ee 0%, #3b7fd0 70%, #a9afb6 72%, #a9afb6 100%); }

  .pill { position: absolute; width: 266px; height: 89px; border-radius: 45px; color: #fff;
    box-shadow: 0 14px 20px rgba(0,0,0,.18); }
  .pill .copy { position: absolute; top: 0; bottom: 0; display: flex; flex-direction: column; justify-content: center; text-align: center; }
  .pill .label { font-size: 10px; line-height: 1.3; }
  .pill .title { font-size: 10px; line-height: 1.35; }
  .pill .desc { font-family: "Hind", sans-serif; font-size: 8px; line-height: 1.45; margin-top: 4px; opacity: .95; }
  .pill .badge { position: absolute; top: 8px; width: 72px; height: 72px; border-radius: 50%;
    background: radial-gradient(circle at 35% 30%, #ffffff 0%, #e9e9e9 70%, #cfcfcf 100%);
    box-shadow: 0 4px 8px rgba(0,0,0,.25); display: flex; align-items: center; justify-content: center; }
  .pill--left .copy { left: 20px; width: 190px; }
  .pill--left .badge { right: 8px; }
  .pill--right .copy { right: 20px; width: 170px; }
  .pill--right .badge { left: 8px; }
  .pill--right .label { font-size: 13px; letter-spacing: .08em; line-height: 1.1; }
  .pill--right .title { font-size: 10px; letter-spacing: .06em; }

  .pill--altitude { left: 160px; top: 287px; background: linear-gradient(180deg, var(--gold-top), var(--gold-bottom)); }
  .pill--altitude .label { color: #111; }
  .pill--agility { left: 160px; top: 467px; background: linear-gradient(180deg, var(--violet-top), var(--violet-bottom)); }
  .pill--agility .label { color: #111; }
  .pill--agency { left: 785px; top: 400px; background: linear-gradient(180deg, var(--rose-top), var(--rose-bottom)); }
  .pill--agency .label { color: #111; }
  .pill--aspiration { left: 785px; top: 533px; background: linear-gradient(180deg, var(--aqua-top), var(--aqua-bottom)); }
  .pill--aspiration .label { color: #111; }

  .step-no { position: absolute; font-size: 24px; font-weight: 300; }
  .step-no--4 { left: 117px; top: 307px; color: var(--gold-top); }
  .step-no--3 { left: 117px; top: 487px; color: #9a72f2; }
  .step-no--2 { left: 1060px; top: 428px; color: var(--rose-line); }
  .step-no--1 { left: 1063px; top: 562px; color: var(--aqua-line); }

  .connectors { position: absolute; left: 0; top: 0; }

  .note { position: absolute; left: 171px; top: 623px; color: var(--brand-red); font-family: "Hind", sans-serif; font-size: 14.5px; line-height: 1.25; }
</style>
</head>
<body>

  <div class="school-mark school-mark--primary">
    <span class="dot"></span>
    <span class="name">Crescent Vale<br>Private School</span>
  </div>
  <div class="school-mark school-mark--community">
    <span class="dot"></span>
    <span class="name">Harbor Ridge<br>Community School</span>
  </div>

  <div class="rule"></div>

  <h1 class="page-title">Envisioning Our<br>Learners</h1>

  <svg class="connectors" width="1200" height="755" viewBox="0 0 1200 755">
    <g fill="none" stroke-width="3">
      <path d="M425 330 H487 L738 288" stroke="var(--gold-line)"/>
      <path d="M425 511 H510" stroke="var(--violet-line)"/>
      <path d="M690 470 L742 445 H786" stroke="var(--rose-line)"/>
      <path d="M688 566 L742 578 H786" stroke="var(--aqua-line)"/>
      <path d="M420 622 L497 621 H548 L588 557" stroke="var(--teal-line)"/>
    </g>
    <g stroke="#fff" stroke-width="3">
      <circle cx="487" cy="330" r="8" fill="#e0901c"/>
      <circle cx="487" cy="511" r="8" fill="#6d3fd6"/>
      <circle cx="742" cy="445" r="8" fill="#e04a8a"/>
      <circle cx="742" cy="578" r="8" fill="#22b8cc"/>
      <circle cx="497" cy="621" r="8" fill="var(--teal-line)"/>
    </g>

    <defs>
      <path id="arc-spirit" d="M562.8 569.3 A70 70 0 0 1 584.9 444.4"/>
      <path id="arc-mind" d="M628.3 442.5 A74 74 0 0 1 667.1 475"/>
      <path id="arc-heart" d="M585.9 600.2 A90 90 0 0 0 656 584.6"/>
    </defs>
    <g fill="none" stroke-width="46">
      <path d="M590 585.9 A75 75 0 0 1 583.6 439.6" stroke="#6035d0"/>
      <path d="M583.6 439.6 A75 75 0 0 1 673.5 537.7" stroke="#e5508e"/>
      <path d="M673.5 537.7 A75 75 0 0 1 590 585.9" stroke="#2fd4e6"/>
    </g>
    <g font-family="Prompt, sans-serif" font-size="13" fill="#fff" letter-spacing="0.6">
      <text><textPath href="#arc-spirit" startOffset="2">Attitude and Spirit</textPath></text>
      <text font-size="14"><textPath href="#arc-mind">MIND</textPath></text>
      <text font-size="14"><textPath href="#arc-heart" startOffset="4">HEART</textPath></text>
    </g>
    <circle cx="603" cy="512" r="51" fill="var(--core)" stroke="#fff" stroke-width="4"/>
    <g font-family="Prompt, sans-serif" font-size="13" fill="#111" text-anchor="middle">
      <text x="603" y="487">Values</text>
      <text x="603" y="505">Morals</text>
      <text x="603" y="523">Principles</text>
      <text x="603" y="541">Ethics</text>
    </g>
  </svg>

  <div class="scene-art scene-art--summit" role="img" aria-label="Illustration of a hiker climbing toward a row of mountain peaks"></div>
  <div class="scene-art scene-art--compass" role="img" aria-label="Illustration of a navigation compass, the metaphorical compass for the four descriptors"></div>

  <div class="step-no step-no--4">4</div>
  <div class="pill pill--left pill--altitude">
    <div class="copy">
      <span class="label">Learners</span>
      <span class="title">with Altitude:</span>
      <span class="desc">Achiefe great things and work to elevate</span>
    </div>
    <div class="badge">
      <svg width="40" height="40" viewBox="0 0 40 40" aria-hidden="true">
        <path d="M8 34 V26 C4 22 4 14 9 9 C14 4 24 4 28 10 L31 18 L28 19 V26 H22 V34 Z" fill="#333"/>
        <circle cx="30" cy="10" r="6" fill="none" stroke="#333" stroke-width="2.5"/>
        <circle cx="30" cy="10" r="2" fill="#333"/>
      </svg>
    </div>
  </div>

  <div class="step-no step-no--3">3</div>
  <div class="pill pill--left pill--agility">
    <div class="copy">
      <span class="label">Learners</span>
      <span class="title">with Agility</span>
      <span class="desc">Are determined, equipped and<br>able to accomplish great things</span>
    </div>
    <div class="badge">
      <svg width="40" height="44" viewBox="0 0 40 44" aria-hidden="true">
        <circle cx="22" cy="6" r="4" fill="#222"/>
        <path d="M20 11 L14 22 L8 28 M16 18 L24 24 L22 32 M19 12 L28 14" stroke="#222" stroke-width="3.5" fill="none" stroke-linecap="round"/>
        <circle cx="12" cy="36" r="4" fill="none" stroke="#f2b51c" stroke-width="3"/>
        <circle cx="28" cy="35" r="5" fill="none" stroke="#27b7d6" stroke-width="3.5"/>
      </svg>
    </div>
  </div>

  <div class="step-no step-no--2">2</div>
  <div class="pill pill--right pill--agency">
    <div class="badge">
      <svg width="44" height="44" viewBox="0 0 44 44" aria-hidden="true">
        <circle cx="22" cy="6" r="4" fill="#333"/>
        <path d="M15 18 C15 12 29 12 29 18 Z" fill="#333"/>
        <path d="M22 18 V24 M6 24 H38 M6 24 V30 M22 24 V30 M38 24 V30" stroke="#333" stroke-width="2.5" fill="none"/>
        <rect x="1" y="31" width="10" height="6" rx="1.5" fill="none" stroke="#333" stroke-width="2.5"/>
        <rect x="17" y="31" width="10" height="6" rx="1.5" fill="none" stroke="#333" stroke-width="2.5"/>
        <rect x="33" y="31" width="10" height="6" rx="1.5" fill="none" stroke="#333" stroke-width="2.5"/>
      </svg>
    </div>
    <div class="copy">
      <span class="label">Leaners</span>
      <span class="title">with Agency</span>
      <span class="desc">Believe in theor capacity and<br>responibility to do great things</span>
    </div>
  </div>

  <div class="step-no step-no--1">1</div>
  <div class="pill pill--right pill--aspiration">
    <div class="badge">
      <svg width="40" height="40" viewBox="0 0 40 40" aria-hidden="true">
        <rect x="3" y="3" width="34" height="18" fill="none" stroke="#333" stroke-width="2.5"/>
        <path d="M7 16 L14 10 L20 14 L32 7" stroke="#333" stroke-width="2" fill="none"/>
        <circle cx="9" cy="27" r="3.5" fill="#333"/>
        <circle cx="20" cy="26" r="4" fill="#333"/>
        <circle cx="31" cy="27" r="3.5" fill="#333"/>
        <path d="M3 38 C3 31 15 31 15 38 Z M13 38 C13 30 27 30 27 38 Z M25 38 C25 31 37 31 37 38 Z" fill="#333"/>
      </svg>
    </div>
    <div class="copy">
      <span class="label">Leaners</span>
      <span class="title">with Aspiration</span>
      <span class="desc">Inspired and Believe in pursuing<br>great things</span>
    </div>
  </div>

  <p class="note">Note: this represents<br>the metaphorical<br>compass for the<br>descriptors 1-4</p>

</body>
</html>
```